Pediatric Vision Care: Myopia Control Brochure

We are a pediatric eye care practice (ophthalmology and optometry). One of our services we offer for children is myopia control, which are strategies for slowing or stopping the progression of nearsightedness. This is a service we need to sell to parents because most insurance won't pay for it. There are different options we offer that can work well for kids in different situations: glasses with Corvane lenses, atropine eye drops, and/or special contact lenses. We need a brochure we can distribute to parents to let them know about this service that would encourage them to buy it for children who need it. Attached is our initial draft brochure created by our staff that provides text that we want to keep. The images and layout can change. We probably need at least one or two photos of kids on the brochure, because this is only something that works for children who are still growing, and the target audience is parents of 4-8 year old children.

Target Market(s)

Parents of 4-8 year old children

Font styles to use
Sans Serif

Requirements
Must have
• I'm uploading our company logo that should be included somewhere on the brochure. You can include contact information (web address, phone number) for our practice that is found on our website: http://www.brookhollowkidsvision.com/
Should not have
• This should not look childish. We need the impression to be friendly but professional, medical, expert.

```html
<!DOCTYPE html>
<html lang="en">
<head>
<meta charset="utf-8">
<title>Myopia Control Brochure – Brookhollow Kids Vision</title>
<link href="https://fonts.googleapis.com/css2?family=Outfit:wght@400;500;600;700&display=swap" rel="stylesheet">
<style>
:root{
  --blue:#1a4fcf;
  --blue-soft:#eaf2fd;
  --green:#4ba52b;
  --green-soft:#eef6e7;
  --orange:#f26a1c;
  --orange-soft:#fff1e8;
  --ink:#2b2f36;
  --paper:#ffffff;
  --stage:#ffffff;
}
*{box-sizing:border-box;margin:0;padding:0}
html,body{width:1200px;height:675px;overflow:hidden;background:var(--stage)}
body{font-family:"Outfit",sans-serif;color:var(--ink);position:relative}
.page{position:absolute;background:var(--paper);box-shadow:0 1px 6px rgba(0,0,0,.18);overflow:hidden}
.page-front{left:78px;top:11px;width:516px;height:650px}
.page-back{left:627px;top:11px;width:495px;height:651px}
.brand{position:absolute;display:flex;align-items:center;gap:8px;color:var(--blue);font-weight:600;font-size:19px;line-height:1.05}
.brand-dot{width:14px;height:14px;border-radius:50%;background:var(--green);flex:none}
.front-brand{left:28px;top:48px}
.photo{position:absolute;left:222px;top:0;width:294px;height:363px;
  background:linear-gradient(90deg,#ffffff 0%,rgba(255,255,255,0) 28%),radial-gradient(ellipse at 62% 52%,#d7b69a 0%,#c9a588 30%,#e3e9de 62%,#f3f5f1 100%)}
.headline{position:absolute;left:24px;top:136px;font-size:60px;font-weight:700;line-height:58px;color:var(--blue);letter-spacing:-.5px}
.rule{position:absolute;left:25px;top:267px;width:38px;height:3px;background:var(--green)}
.tagline{position:absolute;left:26px;top:283px;font-size:18px;line-height:22px;color:#3b3f46}
.card{position:absolute;border-radius:10px}
.card-env{left:25px;top:370px;width:224px;height:213px;background:var(--blue-soft)}
.card-myo{left:260px;top:370px;width:226px;height:213px;background:var(--green-soft)}
.card-head{position:absolute;left:14px;top:13px;display:flex;align-items:center;gap:13px}
.icon-circle{width:54px;height:54px;border-radius:50%;display:flex;align-items:center;justify-content:center;flex:none}
.icon-circle.blue{background:var(--blue)}
.icon-circle.green{background:var(--green)}
.card-title{font-size:19px;font-weight:500;line-height:21px}
.card-env .card-title{color:var(--blue)}
.card-myo .card-title{color:var(--green)}
.card-list{position:absolute;left:20px;top:71px;list-style:none;font-size:13px;line-height:20px;color:#333;white-space:nowrap}
.card-list li::before{content:"•";margin-right:9px;font-size:10px}
.card-text{position:absolute;left:19px;top:74px;font-size:13.2px;line-height:18px;color:#333;white-space:nowrap}
.card-foot{position:absolute;left:0;right:0;top:164px;text-align:center;font-size:15px;font-weight:500;line-height:18px}
.card-env .card-foot{color:var(--blue)}
.card-myo .card-foot{color:var(--green)}
.footer{position:absolute;left:0;right:0;bottom:0;height:52px;background:var(--blue);display:flex;align-items:center;color:#fff;font-size:14px;font-weight:500}
.footer .item{display:flex;align-items:center;gap:10px;flex:1;justify-content:center}
.footer .divider{width:1px;height:26px;background:rgba(255,255,255,.6)}
.back-brand{left:0;right:0;top:38px;justify-content:center}
.back-title{position:absolute;left:0;right:0;top:95px;text-align:center;font-size:21px;font-weight:600;color:var(--blue)}
.back-sub{position:absolute;left:0;right:0;top:122px;text-align:center;font-size:12.8px;line-height:16px;color:#333}
.option{position:absolute;top:189px;height:332px;border-radius:10px;border:1px solid;overflow:hidden;background:#fff}
.opt-lens{left:22px;width:134px;border-color:#9db6ee}
.opt-glasses{left:166px;width:147px;border-color:#a9d591}
.opt-drops{left:323px;width:146px;border-color:#f6b48c}
.opt-icon{position:absolute;top:165px;width:64px;height:64px;border-radius:50%;display:flex;align-items:center;justify-content:center}
.opt-name{position:absolute;left:0;right:0;top:46px;text-align:center;font-size:18px;font-weight:500;line-height:21px}
.opt-list{position:absolute;left:11px;top:117px;list-style:none;font-size:11.6px;line-height:14.7px;color:#333;white-space:nowrap}
.opt-list li{padding-left:13px;position:relative;margin-bottom:5.3px}
.opt-list li::before{content:"•";position:absolute;left:0;font-size:9px}
.opt-foot{position:absolute;left:0;right:0;bottom:0;height:72px;display:flex;align-items:center;justify-content:center;text-align:center;font-size:13px;font-weight:500;line-height:16px;white-space:nowrap}
.opt-lens .opt-name,.opt-lens .opt-foot{color:var(--blue)}
.opt-lens .opt-foot{background:var(--blue-soft)}
.opt-glasses .opt-name,.opt-glasses .opt-foot{color:var(--green)}
.opt-glasses .opt-foot{background:var(--green-soft)}
.opt-drops .opt-name,.opt-drops .opt-foot{color:var(--orange)}
.opt-drops .opt-foot{background:var(--orange-soft)}
.opt-drops .opt-name{top:58px}
.personal{position:absolute;left:30px;top:528px;display:flex;align-items:center;gap:19px}
.personal-icon{width:64px;height:64px;border-radius:50%;border:2px solid var(--blue);display:flex;align-items:center;justify-content:center;flex:none}
.personal h3{font-size:16.3px;font-weight:500;color:var(--blue);line-height:20px}
.personal p{font-size:13px;line-height:16px;color:#333;white-space:nowrap}
</style>
</head>
<body>

<section class="page page-front">
  <div class="brand front-brand"><span class="brand-dot"></span>Brookhollow<br>Kids Vision</div>
  <div class="photo" role="img" aria-label="Photo of a smiling child wearing dark-framed glasses, looking upward"></div>
  <h1 class="headline">Myopia<br>Control</h1>
  <div class="rule"></div>
  <p class="tagline">Protect your child’s<br>vision today for a<br>brighter tomorrow.</p>

  <div class="card card-env">
    <div class="card-head">
      <div class="icon-circle blue">
        <svg width="30" height="30" viewBox="0 0 30 30" fill="none" stroke="#fff" stroke-width="1.8" stroke-linecap="round"><path d="M11 4c-4 0-6 4-5 7-2 2-1 6 2 6h6c3 0 4-4 2-6 1-3-1-7-5-7z"/><path d="M11 17v9M5 26h21M17 21h9M18 21v5M25 21v5"/></svg>
      </div>
      <h2 class="card-title">Environmental<br>options</h2>
    </div>
    <ul class="card-list">
      <li>Increase outdoor time</li>
      <li>Reduce screen time</li>
      <li>Promote good lighting</li>
      <li>Encourage regular breaks</li>
    </ul>
    <p class="card-foot">Small changes.<br>Big impact.</p>
  </div>

  <div class="card card-myo">
    <div class="card-head">
      <div class="icon-circle green">
        <svg width="34" height="22" viewBox="0 0 34 22" fill="none" stroke="#fff" stroke-width="2.2"><path d="M2 11C8 2 26 2 32 11 26 20 8 20 2 11z"/><circle cx="17" cy="11" r="5"/><circle cx="17" cy="11" r="1.5" fill="#fff"/></svg>
      </div>
      <h2 class="card-title">Myopia<br>control</h2>
    </div>
    <p class="card-text">Evidence-based solutions<br>designed to slow the<br>progression of myopia and<br>protect long-term vision.</p>
    <p class="card-foot">Personalized care.<br>Proven results.</p>
  </div>

  <footer class="footer">
    <div class="item">
      <svg width="20" height="20" viewBox="0 0 20 20" fill="none" stroke="#fff" stroke-width="1.5"><circle cx="10" cy="10" r="8.5"/><ellipse cx="10" cy="10" rx="3.8" ry="8.5"/><path d="M1.5 10h17M3 5.5h14M3 14.5h14"/></svg>
      www.brookhollowkidsvision.com
    </div>
    <div class="divider"></div>
    <div class="item">
      <svg width="24" height="24" viewBox="0 0 24 24"><circle cx="12" cy="12" r="12" fill="#fff"/><path d="M8.2 6.5l2 2.8-1.2 1.4c.9 1.8 2.3 3.2 4.1 4.1l1.4-1.2 2.8 2-1 2c-5-.5-9.5-5-10-10z" fill="#1a4fcf"/></svg>
      (555) 214-0382
    </div>
  </footer>
</section>

<section class="page page-back">
  <div class="brand back-brand"><span class="brand-dot"></span>Brookhollow<br>Kids Vision</div>
  <h2 class="back-title">Myopia Control Treatment Options</h2>
  <p class="back-sub">We offer a range of effective, evidence-based treatments<br>to help slow the progression of myopia in children.</p>

  <div class="option opt-lens">
    <h3 class="opt-name">Soft<br>Contact<br>Lenses</h3>
    <ul class="opt-list">
      <li>FDA-approved<br>for myopia control</li>
      <li>Worn daily</li>
      <li>Clinically proven<br>to slow myopia<br>progression</li>
      <li>Safe, effective,<br>and non-surgical</li>
    </ul>
    <p class="opt-foot">A comfortable<br>choice with<br>proven results.</p>
  </div>
  <div class="opt-icon" style="left:57px;background:var(--blue)">
    <svg width="36" height="30" viewBox="0 0 36 30" fill="none" stroke="#fff" stroke-width="2"><path d="M3 24C5 10 20 2 33 5 31 18 17 28 3 24z"/><path d="M8 21c4-7 11-11 19-12"/></svg>
  </div>

  <div class="option opt-glasses">
    <h3 class="opt-name">Specialty<br>Eyeglass<br>Lenses</h3>
    <ul class="opt-list">
      <li>Designed to slow<br>eye growth</li>
      <li>Easy and non-invasive</li>
      <li>Ideal for full-time<br>wear</li>
      <li>Effective for many<br>children</li>
    </ul>
    <p class="opt-foot">Everyday eyewear<br>with long-term<br>benefits.</p>
  </div>
  <div class="opt-icon" style="left:208px;background:var(--green)">
    <svg width="40" height="20" viewBox="0 0 40 20" fill="none" stroke="#fff" stroke-width="2.4"><rect x="4" y="5" width="13" height="11" rx="5"/><rect x="23" y="5" width="13" height="11" rx="5"/><path d="M17 9c2-2 4-2 6 0M4 8L1 5M36 8l3-3"/></svg>
  </div>

  <div class="option opt-drops">
    <h3 class="opt-name">Atropine<br>Eye Drops</h3>
    <ul class="opt-list">
      <li>Low-dose atropine<br>drops</li>
      <li>Applied once daily<br>at night</li>
      <li>Clinically shown<br>to slow myopia<br>progression</li>
      <li>Easy and safe</li>
    </ul>
    <p class="opt-foot">A simple drop<br>with powerful<br>protection.</p>
  </div>
  <div class="opt-icon" style="left:364px;background:var(--orange)">
    <svg width="34" height="34" viewBox="0 0 34 34" fill="none" stroke="#fff" stroke-width="2" stroke-linejoin="round"><path d="M22 4l8 8-3 3-8-8z"/><path d="M20 10L9 21l-2 5 5-2 11-11"/><path d="M5 28c0 2-1 3-2 3s-2-1-2-3 2-4 2-4 2 2 2 4z" fill="#fff"/></svg>
  </div>

  <div class="personal">
    <div class="personal-icon">
      <svg width="40" height="30" viewBox="0 0 40 30" fill="none" stroke="#1a4fcf" stroke-width="1.8"><circle cx="20" cy="7" r="4.5"/><circle cx="9" cy="10" r="3.5"/><circle cx="31" cy="10" r="3.5"/><path d="M11 27c0-6 4-10 9-10s9 4 9 10M2 26c0-5 3-8 7-8 2 0 3 .5 4 1.5M38 26c0-5-3-8-7-8-2 0-3 .5-4 1.5"/></svg>
    </div>
    <div>
      <h3>Personalized Myopia Management</h3>
      <p>Every child’s eyes are different. We’ll help you choose<br>the right option for your child’s unique needs.</p>
    </div>
  </div>

  <footer class="footer">
    <div class="item">
      <svg width="20" height="20" viewBox="0 0 20 20" fill="none" stroke="#fff" stroke-width="1.5"><circle cx="10" cy="10" r="8.5"/><ellipse cx="10" cy="10" rx="3.8" ry="8.5"/><path d="M1.5 10h17M3 5.5h14M3 14.5h14"/></svg>
      www.brookhollowkidsvision.com
    </div>
    <div class="divider"></div>
    <div class="item">
      <svg width="24" height="24" viewBox="0 0 24 24"><circle cx="12" cy="12" r="12" fill="#fff"/><path d="M8.2 6.5l2 2.8-1.2 1.4c.9 1.8 2.3 3.2 4.1 4.1l1.4-1.2 2.8 2-1 2c-5-.5-9.5-5-10-10z" fill="#1a4fcf"/></svg>
      (555) 214-0382
    </div>
  </footer>
</section>

</body>
</html>
```